Marwick Ostrand Law website for a law firm

modern clean website for a small boutique law firm. Based in Sacramento, CA and the Bay Area. Practice areas of Family Law, Civil litigation, and Criminal Defense. We already have a logo design as well as attorney pictures to include on page.
Would like images of California included on site.
Would like site to go with Logo that is already designed...blue/grey/white colors.

Industry/Entity Type

Law Firm

Number of Pages Required

5+ page

Requirements
Must have
• I already have several pages of content drafted. Just need the pages with images to input content. Must be clean and modern feel. Want it to reflect California and small boutique feel that is provided personalized legal attention.
• Must have a page where I can blog or post articles on.

```html
<!DOCTYPE html>
<html lang="en">
<head>
<meta charset="utf-8">
<title>Marwick Ostrand Law</title>
<link href="https://fonts.googleapis.com/css2?family=Gelasio:wght@400;700&family=Tinos:wght@400;700&family=Montserrat:wght@300;400&display=swap" rel="stylesheet">
<style>
:root{
  --blue:#4a86c8;
  --blue-dark:#1f4f82;
  --grey-bar:#8d8d8d;
  --ink:#222;
  --text:#444;
  --white:#fff;
}
*{margin:0;padding:0;box-sizing:border-box}
html,body{width:1200px;height:2539px;overflow:hidden;background:var(--white)}
body{position:relative;font-family:"Tinos",serif;color:var(--text)}
.abs{position:absolute}

/* top bar */
.topbar{left:0;top:0;width:1200px;height:41px;background:var(--grey-bar)}
.topbar-blue{left:0;top:0;width:600px;height:41px;background:var(--blue);clip-path:polygon(0 0,100% 0,96% 100%,0 100%)}
.topbar-info{right:86px;top:0;height:41px;display:flex;align-items:center;gap:22px;font-family:"Montserrat",sans-serif;font-size:15px;color:var(--white)}
.topbar-info span{display:flex;align-items:center;gap:6px}
.social{display:flex;gap:12px;align-items:center}
.social i{display:block;width:11px;height:11px;border-radius:50%;background:currentColor}

/* header */
.brand{left:86px;top:0;width:261px;height:102px;background:var(--white);box-shadow:0 6px 12px rgba(0,0,0,.15);display:flex;align-items:center;justify-content:center;z-index:3;font-family:"Tinos",serif;font-weight:700;font-size:24px;color:var(--blue-dark)}
.nav{top:74px;left:0;width:1200px;height:26px;font-family:"Tinos",serif;font-size:16px;color:#333;z-index:3}
.nav a{position:absolute;text-decoration:none;color:inherit;white-space:nowrap}
.nav a.active{color:var(--blue)}

/* hero */
.hero{left:0;top:0;width:1200px;height:669px;background:
  radial-gradient(ellipse at 30% 40%,rgba(255,240,220,.9),rgba(255,240,220,0) 35%),
  linear-gradient(180deg,#8fc4ea 0%,#b9d8ee 38%,#e0cfb4 52%,#4d8db0 60%,#3d7aa0 72%,#6b8e52 88%,#a7a44c 100%)}
.hero-welcome{left:0;top:304px;width:1200px;text-align:center;font-family:"Gelasio",serif;font-size:31px;color:#1f63a8}
.hero-title{left:0;top:350px;width:1200px;text-align:center;font-family:"Gelasio",serif;font-weight:700;font-size:44px;color:var(--white);letter-spacing:1px;text-shadow:0 2px 6px rgba(0,0,0,.25)}

/* about */
.about-photo{left:675px;top:580px;width:439px;height:441px;background:linear-gradient(135deg,#9a4a32 0%,#7a3d2a 45%,#3b3f4a 70%,#2b2b30 100%)}
.about-photo-frame{left:689px;top:594px;width:411px;height:413px;border:1px solid rgba(255,255,255,.85)}
.section-title{font-family:"Gelasio",serif;font-weight:700;color:var(--ink)}
.about-title{left:86px;top:722px;font-size:30px}
.rule{height:4px;width:60px;background:var(--blue);border-radius:2px}
.about-rule{left:86px;top:768px}
.about-text{left:86px;top:795px;width:545px;font-size:14.5px;line-height:23px;color:#444}
.about-text p+p{margin-top:15px}
.btn-solid{left:86px;top:982px;width:122px;height:37px;background:var(--blue);color:var(--white);font-size:15px;display:flex;align-items:center;justify-content:center}

/* practice */
.practice-fade{left:0;top:1015px;width:320px;height:505px;background:radial-gradient(ellipse at 35% 30%,rgba(200,200,200,.35),rgba(255,255,255,0) 70%)}
.practice-title{left:0;top:1075px;width:1200px;text-align:center;font-size:30px}
.practice-rule{left:570px;top:1125px}
.card{top:1170px;width:325px}
.card-img{width:325px;height:199px}
.card-icon{position:absolute;left:139px;top:160px;width:47px;height:47px;border-radius:50%;background:var(--white);display:flex;align-items:center;justify-content:center}
.card h3{margin-top:20px;text-align:center;font-family:"Gelasio",serif;font-weight:700;font-size:25px;color:var(--ink)}
.card p{margin-top:14px;text-align:center;font-size:14px;line-height:23px;color:#444;padding:0 8px}
.btn-outline{display:block;margin:18px auto 0;width:61px;height:26px;border:1px solid var(--blue);color:var(--blue);font-size:13px;text-align:center;line-height:24px}

/* contact */
.contact{left:0;top:1621px;width:1200px;height:667px;background:
  radial-gradient(ellipse at 50% 45%,rgba(90,95,100,.55),rgba(30,34,38,0) 55%),
  linear-gradient(180deg,#15191d 0%,#22282d 60%,#181c20 100%)}
.contact-title{left:0;top:1664px;width:1200px;text-align:center;font-family:"Gelasio",serif;font-weight:700;font-size:27px;color:var(--white)}
.contact-rule{left:570px;top:1712px}
.label{font-size:14px;color:var(--white)}
.field{border:1px solid rgba(255,255,255,.35);background:rgba(255,255,255,.12)}
.select-text{font-size:13px;color:#ddd;padding:14px 0 0 14px}
.select-arrow{right:0;top:0;width:52px;height:100%;border-left:1px solid rgba(255,255,255,.35);display:flex;align-items:center;justify-content:center}
.btn-send{left:526px;top:2195px;width:148px;height:42px;border:1px solid var(--blue);color:var(--blue);font-size:15px;display:flex;align-items:center;justify-content:center;letter-spacing:.5px}

/* footer */
.footer{left:0;top:2288px;width:1200px;height:197px;background:var(--blue)}
.footer-box{top:2302px;width:284px;height:169px;border:1px solid rgba(255,255,255,.7);display:flex;flex-direction:column;align-items:center;justify-content:center;color:var(--white);font-size:16px;line-height:24px;text-align:center}
.footer-box svg{margin-bottom:10px}
.bottombar{left:0;top:2485px;width:1200px;height:54px;background:var(--blue-dark);display:flex;align-items:center;justify-content:space-between;padding:0 86px;font-family:"Montserrat",sans-serif;font-size:11px;color:#cfe0f3}
.bottombar .social{gap:20px}
.bottombar .social i{width:13px;height:13px}
</style>
</head>
<body>

<div class="abs hero" role="img" aria-label="Photo of the Golden Gate Bridge over the bay at sunset with green hills"></div>
<div class="abs topbar"></div>
<div class="abs topbar-blue"></div>
<div class="abs topbar-info">
  <span><svg width="13" height="13" viewBox="0 0 24 24" fill="#fff"><path d="M6.6 10.8a15.1 15.1 0 0 0 6.6 6.6l2.2-2.2a1 1 0 0 1 1-.25 11.4 11.4 0 0 0 3.6.57 1 1 0 0 1 1 1V20a1 1 0 0 1-1 1A17 17 0 0 1 3 4a1 1 0 0 1 1-1h3.5a1 1 0 0 1 1 1c0 1.25.2 2.45.57 3.57a1 1 0 0 1-.25 1z"/></svg>(925) 555-0142</span>
  <span><svg width="14" height="13" viewBox="0 0 24 22" fill="#fff"><path d="M12 0 0 8v14h24V8zm0 3 9 6-9 6-9-6z"/></svg>info@marwickostrand.com</span>
  <span class="social"><i></i><i></i><i></i></span>
</div>

<div class="abs brand">Marwick Ostrand Law</div>
<nav class="abs nav">
  <a class="active" style="left:421px">Home</a>
  <a style="left:505px">About Us</a>
  <a style="left:613px">Clara J. Marwick</a>
  <a style="left:767px">Dev A. Ostrand</a>
  <a style="left:902px">Practice Areas &#8964;</a>
  <a style="left:1058px">Contact</a>
</nav>

<div class="abs hero-welcome">Welcome to</div>
<h1 class="abs hero-title">MARWICK OSTRAND LAW</h1>

<div class="abs about-photo" role="img" aria-label="Portrait of the two founding attorneys in front of a brick wall"></div>
<div class="abs about-photo-frame"></div>
<h2 class="abs section-title about-title">Marwick Ostrand Law</h2>
<div class="abs rule about-rule"></div>
<div class="abs about-text">
  <p>Marwick Ostrand Law is a boutique business law firm representing small and midsize companies throughout Northern California. Our team of business law attorneys has substantial litigation and transactional experience. After earning his L.L.M. in Transnational Business Practices, our founding partner, Dev Ostrand, dedicated his legal career to business transactions and civil litigation.</p>
  <p>Our firm is involved in every aspect of a business's formation, management and growth.</p>
</div>
<div class="abs btn-solid">Learn More &raquo;</div>

<div class="abs practice-fade" role="img" aria-label="Faded portrait of an attorney in the background"></div>
<h2 class="abs section-title practice-title">Our Practice Areas</h2>
<div class="abs rule practice-rule"></div>

<div class="abs card" style="left:86px">
  <div style="position:relative">
    <div class="card-img" role="img" aria-label="Photo of a handshake above brass scales of justice" style="background:linear-gradient(135deg,#111 0%,#3a3a3a 45%,#8a7a5a 60%,#1a1a1a 100%)"></div>
    <div class="card-icon"><svg width="26" height="26" viewBox="0 0 24 24" fill="var(--blue)"><rect x="9" y="2" width="8" height="5" transform="rotate(45 13 4.5)"/><rect x="5" y="10" width="3" height="11" transform="rotate(-45 6.5 15.5)"/><rect x="3" y="20" width="12" height="3"/></svg></div>
  </div>
  <h3>Business Law</h3>
  <p>Marwick Ostrand Law is a boutique business law firm representing small and midsize companies throughout Northern California</p>
  <span class="btn-outline">MORE</span>
</div>

<div class="abs card" style="left:437px">
  <div style="position:relative">
    <div class="card-img" role="img" aria-label="Photo of a blue binder labelled for family law on a desk with a pen" style="background:linear-gradient(180deg,#d9dde2 0%,#3b6fb0 35%,#2f5f9e 62%,#e7e7e7 70%,#cfcfcf 100%)"></div>
    <div class="card-icon"><svg width="26" height="26" viewBox="0 0 24 24" fill="var(--blue)"><rect x="9" y="2" width="8" height="5" transform="rotate(45 13 4.5)"/><rect x="5" y="10" width="3" height="11" transform="rotate(-45 6.5 15.5)"/><rect x="3" y="20" width="12" height="3"/></svg></div>
  </div>
  <h3>Family Law</h3>
  <p>Marwick Ostrand Law offers a dedicated and highly skilled family law practice in Sacramento. Our attorneys leverage substantial family litigation</p>
  <span class="btn-outline">MORE</span>
</div>

<div class="abs card" style="left:789px">
  <div style="position:relative">
    <div class="card-img" role="img" aria-label="Photo of handcuffed hands resting on a wooden table" style="background:linear-gradient(180deg,#b9cbe0 0%,#c99a80 40%,#7a5236 70%,#5a3b28 100%)"></div>
    <div class="card-icon"><svg width="26" height="26" viewBox="0 0 24 24" fill="var(--blue)"><rect x="9" y="2" width="8" height="5" transform="rotate(45 13 4.5)"/><rect x="5" y="10" width="3" height="11" transform="rotate(-45 6.5 15.5)"/><rect x="3" y="20" width="12" height="3"/></svg></div>
  </div>
  <h3>Criminal Defense</h3>
  <p>Marwick Ostrand Law offers a dedicated and highly skilled family law practice in Sacramento. Our attorneys leverage substantial family litigation</p>
  <span class="btn-outline">MORE</span>
</div>

<div class="abs contact" role="img" aria-label="Dark photo of the California State Capitol dome framed by palm trees"></div>
<h2 class="abs contact-title">Contact Us</h2>
<div class="abs rule contact-rule"></div>

<div class="abs label" style="left:86px;top:1747px">Name</div>
<div class="abs field" style="left:86px;top:1769px;width:498px;height:45px"></div>
<div class="abs label" style="left:616px;top:1747px">Email</div>
<div class="abs field" style="left:616px;top:1769px;width:498px;height:45px"></div>

<div class="abs label" style="left:86px;top:1836px">Subject</div>
<div class="abs field" style="left:86px;top:1857px;width:1028px;height:45px"></div>

<div class="abs label" style="left:86px;top:1925px">Select your service</div>
<div class="abs field" style="left:86px;top:1946px;width:498px;height:48px">
  <div class="select-text">- Select your service -</div>
  <div class="abs select-arrow"><svg width="16" height="12" viewBox="0 0 16 12"><path d="M0 0h16L8 12z" fill="#eee"/></svg></div>
</div>
<div class="abs label" style="left:616px;top:1925px">Booking Date (MM/DD/YY)</div>
<div class="abs field" style="left:616px;top:1946px;width:498px;height:48px"></div>

<div class="abs label" style="left:86px;top:2021px">Message</div>
<div class="abs field" style="left:86px;top:2043px;width:1028px;height:108px"></div>

<div class="abs btn-send">SEND MESSAGE</div>

<div class="abs footer"></div>
<div class="abs footer-box" style="left:105px">
  <svg width="32" height="32" viewBox="0 0 24 24" fill="#fff"><path d="M22 2 2 10.5l8.5 3L13.5 22z"/></svg>
  <div>Sacramento Area Office:<br>410 Elm St, Suite 200<br>Sacramento, CA 95814</div>
</div>
<div class="abs footer-box" style="left:457px">
  <svg width="32" height="32" viewBox="0 0 24 24" fill="#fff"><path d="M6.6 10.8a15.1 15.1 0 0 0 6.6 6.6l2.2-2.2a1 1 0 0 1 1-.25 11.4 11.4 0 0 0 3.6.57 1 1 0 0 1 1 1V20a1 1 0 0 1-1 1A17 17 0 0 1 3 4a1 1 0 0 1 1-1h3.5a1 1 0 0 1 1 1c0 1.25.2 2.45.57 3.57a1 1 0 0 1-.25 1z"/></svg>
  <div>(916) 555-0187<br>&amp;<br>(925) 555-0142</div>
</div>
<div class="abs footer-box" style="left:809px">
  <svg width="36" height="34" viewBox="0 0 24 22" fill="#fff"><path d="M12 0 0 8v14h24V8zm0 3 9 6-9 6-9-6z"/></svg>
  <div>info@marwickostrand.com</div>
</div>

<div class="abs bottombar">
  <span>Copyright 2017 Your Company Name Here</span>
  <span class="social"><i></i><i></i><i></i></span>
</div>

</body>
</html>
```